Real Estate Listing Signs for standard Yard arms

I need real estate listing signs done, for the standard sized sign to be hung beneath a white yard arm. To match existing logo. Information to be included:
-Logo
-Business name
-Phone number
-Dorran Fitch Tundra Circle & Dorran Fitch realty logos (smaller print)

Colors to be Red and anywhere in the gray scale between black and white, or a combination of those.

Target Market(s)

Drive by visuals

Industry/Entity Type

Real Estate Agent

Colors

Designer to choose only greyscale colors for use in the design.

Requirements
Must have
• My Logo and business name in same/similar font to whats provided, the DF tundra circle logo (small on bottom or corner somewhere), My phone number, and a decent amount of red coloration on the sign.

```html
<!DOCTYPE html>
<html lang="en">
<head>
<meta charset="utf-8">
<title>Marwick Realty — Yard Arm Listing Sign</title>
<link rel="stylesheet" href="https://fonts.googleapis.com/css2?family=Cinzel:wght@700;900&family=Barlow+Condensed:wght@600&display=swap">
<style>
  :root {
    --brand-red: #ff1d25;
    --sign-white: #ffffff;
    --ink-black: #111111;
    --broker-grey: #4a4a4a;
    --broker-grey-light: #6b6b6b;
    --backdrop: #e6e7e9;
  }
  * { margin: 0; padding: 0; box-sizing: border-box; }
  html, body {
    width: 1200px;
    height: 1200px;
    overflow: hidden;
    background: var(--backdrop);
  }
  .canvas {
    position: relative;
    width: 1200px;
    height: 1200px;
  }
  .listing-sign {
    position: absolute;
    left: 178px;
    top: 40px;
    width: 845px;
    height: 1120px;
    background: var(--sign-white);
    box-shadow: 0 6px 22px rgba(0,0,0,0.12);
  }
  .sign-frame {
    position: absolute;
    left: 0;
    top: 0;
    width: 845px;
    height: 1120px;
  }
  .broker-tag {
    position: absolute;
    left: 263px;
    width: 332px;
    top: 58px;
    text-align: center;
    font-family: "Barlow Condensed", "Arial Narrow", sans-serif;
    font-weight: 600;
    line-height: 1;
  }
  .broker-tag__group {
    display: block;
    font-size: 30px;
    letter-spacing: 0.5px;
    color: var(--broker-grey);
  }
  .broker-tag__firm {
    display: block;
    margin-top: 5px;
    font-size: 15px;
    letter-spacing: 1px;
    color: var(--broker-grey-light);
  }
  .brand-mark {
    position: absolute;
    left: 329px;
    top: 305px;
    width: 220px;
    height: 220px;
    background: var(--brand-red);
  }
  .business-name {
    position: absolute;
    left: 0;
    width: 845px;
    top: 600px;
    text-align: center;
    font-family: "Cinzel", Georgia, serif;
    font-weight: 900;
    font-size: 68px;
    line-height: 74px;
    letter-spacing: 2px;
    color: var(--ink-black);
  }
  .phone-number {
    position: absolute;
    left: 0;
    width: 845px;
    top: 905px;
    text-align: center;
    font-family: "Cinzel", Georgia, serif;
    font-weight: 900;
    font-size: 72px;
    line-height: 1;
    letter-spacing: 1px;
    color: var(--ink-black);
  }
</style>
</head>
<body>
  <main class="canvas">
    <section class="listing-sign" aria-label="Marwick Realty listing sign">
      <svg class="sign-frame" viewBox="0 0 845 1120" aria-hidden="true">
        <g fill="var(--brand-red)">
          <!-- left top bar segment -->
          <rect x="36" y="55" width="227" height="44"/>
          <!-- right top bar segment -->
          <rect x="595" y="55" width="210" height="44"/>
          <!-- left side -->
          <rect x="36" y="55" width="45" height="1023"/>
          <!-- right side -->
          <rect x="760" y="55" width="45" height="1023"/>
          <!-- bottom -->
          <rect x="36" y="1034" width="769" height="44"/>
        </g>
      </svg>

      <div class="broker-tag">
        <span class="broker-tag__group">DF TUNDRA CIRCLE</span>
        <span class="broker-tag__firm">DORRAN FITCH REALTY</span>
      </div>

      <div class="brand-mark" aria-hidden="true"></div>

      <h1 class="business-name">MARWICK<br>REALTY</h1>

      <p class="phone-number">907-555-0148</p>
    </section>
  </main>
</body>
</html>
```